Broschüre
Zielgruppe
Firmen und Privatpersonen
Unsere Zielkunden sind im bereich Firmen
Firmen die etwas für die Umwelt tun wollen oder sich einen Grünen anstrich geben wollen
Privatpersonen hier ist es die Gruppe die sich für den erhalt der Natur einsetzten die Bienen oder Naturprojekte unterstützen wollen und dergleichen. In der regel Menschen die BIO Kaufen
Aufgabenstellung
Standard Falzflyer DIN-A4 4 Seiten / Logo vorhanden / Unbedingt noch ein Freifeld zum ausfüllen zum bestellen. Daten die wir zum bestellen benötigen Name/Adresse/Telefonnummer/E-Mail/Unterschrift

```html
<!DOCTYPE html>
<html lang="de">
<head>
<meta charset="utf-8">
<title>Summwerk – Flyer Vorderseite</title>
<link rel="stylesheet" href="https://fonts.googleapis.com/css2?family=Crimson+Text:wght@400;700&display=swap">
<style>
  :root {
    --honey: #fdd56a;
    --rule: #3a3226;
    --paper: #ffffff;
    --brand-red: #c8352b;
    --ink: #141210;
    --hive-wood: #c9a777;
    --hive-shadow: #8c6e48;
    --board-light: #e9dcc6;
    --haze: #f3ede2;
    --meadow: #b5c98a;
    --meadow-deep: #7d9e4c;
  }
  html, body {
    margin: 0;
    padding: 0;
    width: 972px;
    height: 1200px;
    overflow: hidden;
    background: var(--paper);
  }
  .flyer-front {
    position: relative;
    width: 972px;
    height: 1200px;
    overflow: hidden;
    font-family: "Crimson Text", Georgia, serif;
    color: var(--ink);
  }
  .top-band {
    position: absolute;
    left: 0; top: 0;
    width: 970px; height: 70px;
    background: var(--honey);
    border-bottom: 2px solid var(--rule);
    border-right: 2px solid var(--rule);
  }
  .logo-strip {
    position: absolute;
    left: 0; top: 72px;
    width: 970px; height: 164px;
    background: var(--paper);
    border-right: 2px solid var(--rule);
  }
  .brand {
    position: absolute;
    left: 34px; top: 30px;
    display: flex;
    align-items: center;
    gap: 14px;
  }
  .brand-mark {
    width: 92px; height: 92px;
    border-radius: 50%;
    background: var(--honey);
  }
  .brand-name {
    font-weight: 700;
    font-size: 46px;
    color: var(--brand-red);
    margin-top: 22px;
  }
  .divider-band {
    position: absolute;
    left: 0; top: 236px;
    width: 970px; height: 16px;
    background: var(--honey);
    border-top: 2px solid var(--rule);
    border-bottom: 2px solid var(--rule);
    border-right: 2px solid var(--rule);
  }
  .hero-photo {
    position: absolute;
    left: 0; top: 256px;
    width: 972px; height: 944px;
    background:
      radial-gradient(ellipse 48% 30% at 45% 44%, rgba(250,246,238,0.85) 0%, rgba(250,246,238,0) 100%),
      radial-gradient(ellipse 40% 14% at 28% 63%, rgba(110,90,62,0.45) 0%, rgba(110,90,62,0) 100%),
      linear-gradient(170deg, rgba(0,0,0,0) 60%, var(--board-light) 66%, #d8c8ad 80%, rgba(0,0,0,0) 84%),
      radial-gradient(ellipse 30% 50% at 12% 30%, var(--hive-wood) 0%, rgba(201,167,119,0) 100%),
      radial-gradient(ellipse 35% 35% at 82% 88%, var(--meadow-deep) 0%, rgba(125,158,76,0) 100%),
      radial-gradient(ellipse 30% 40% at 88% 20%, #a9bf83 0%, rgba(169,191,131,0) 100%),
      linear-gradient(95deg, var(--hive-shadow) 0%, var(--hive-wood) 14%, var(--haze) 42%, #dfe3c8 60%, var(--meadow) 82%, #9fbb6e 100%);
  }
  .headline {
    position: absolute;
    left: 0; top: 558px;
    width: 972px;
    margin: 0;
    text-align: center;
    font-weight: 400;
    font-size: 71px;
    line-height: 81px;
    letter-spacing: -0.5px;
    color: var(--ink);
  }
  .page-label {
    position: absolute;
    right: 68px; top: 1156px;
    font-size: 20px;
    color: var(--ink);
  }
</style>
</head>
<body>
  <main class="flyer-front">
    <div class="top-band"></div>
    <header class="logo-strip">
      <div class="brand">
        <span class="brand-mark"></span>
        <span class="brand-name">Summwerk</span>
      </div>
    </header>
    <div class="divider-band"></div>
    <div class="hero-photo" role="img" aria-label="Foto: viele Bienen schwärmen vor dem Flugloch eines hölzernen Bienenstocks mit hellem Anflugbrett, grüner unscharfer Wiesenhintergrund"></div>
    <h1 class="headline">Imker auf Zeit - jetzt kann jeder<br>etwas Gutes für die Biene tun!</h1>
    <div class="page-label">Vorderseite</div>
  </main>
</body>
</html>
```